The Marlowe Legal Group, P.C.
Business Cards, Stationary & Email Signature & Letterhead
Use same font as used in my logo
Ruth Benning
Attorney
2847 Tamworth Lane
Suite 3405
Harlow Ridge, GA 30582
ruthbenningesq@quillpost.net
www.marlowelegaloffice.com
Logo + whatever
Ai file of my logo for Stationary project

```html
<!DOCTYPE html>
<html lang="en">
<head>
<meta charset="utf-8">
<title>The Marlowe Legal Group, P.C. — Stationery</title>
<link rel="stylesheet" href="https://fonts.googleapis.com/css2?family=Cormorant+Garamond:wght@600&family=Open+Sans:wght@400;600&display=swap">
<style>
:root{
  --navy:#1f3a8c;
  --navy-dark:#17306f;
  --paper:#ffffff;
  --grey:#9aa0aa;
  --grey-light:#d9dce2;
  --ink:#555b66;
  --bg:#eeeae4;
}
*{box-sizing:border-box;margin:0;padding:0}
html,body{width:1200px;height:698px;overflow:hidden;background:var(--bg)}
body{position:relative;font-family:"Open Sans",sans-serif;color:var(--ink)}
.sheet{position:absolute;background:var(--paper);box-shadow:0 2px 5px rgba(0,0,0,.18);overflow:hidden}
.sheet.blue{background:var(--navy)}
.brand{display:flex;align-items:center;gap:5px;font-family:"Cormorant Garamond",serif;font-weight:600;color:var(--navy);line-height:1.05;text-transform:uppercase}
.brand .dot{border-radius:50%;background:var(--navy);flex:none}
.blue .brand{color:#fff}
.blue .brand .dot{background:#fff}
.brand small{display:block;font-size:.55em;letter-spacing:.06em}
.brand b{display:block;font-weight:600}
.stripe{position:absolute;left:0;right:0;bottom:0;height:7px;background:var(--navy)}
.stripe::after{content:"";position:absolute;right:0;top:-3px;width:35%;height:3px;background:var(--grey)}
.info{position:absolute;font-size:5px;line-height:1.55;color:var(--ink)}
.info strong{color:var(--navy);font-weight:600;font-size:6px}
.rule{position:absolute;width:1px;background:var(--grey-light)}
.fax-title{position:absolute;right:18px;top:58px;font-size:15px;font-weight:600;color:var(--navy)}
.fax-grid{position:absolute;left:18px;right:18px;top:82px;display:grid;grid-template-columns:repeat(4,1fr);gap:3px}
.fax-grid span{font-size:5px;background:var(--grey-light);padding:3px;color:var(--ink)}
.fax-grid span:nth-child(odd){background:#c4c8d0}
.checks{position:absolute;left:18px;right:18px;top:140px;display:flex;justify-content:space-between;font-size:5px}
.checks span::before{content:"";display:inline-block;width:5px;height:5px;border:1px solid var(--grey);margin-right:2px;vertical-align:middle}
.flap{position:absolute}
</style>
</head>
<body>

<!-- business card front -->
<div class="sheet card" style="left:67px;top:82px;width:190px;height:98px">
  <div class="brand" style="position:absolute;left:10px;top:28px;font-size:12px"><span class="dot" style="width:16px;height:16px"></span><span><small>The</small><b>Marlowe</b><small>Legal Group, P.C.</small></span></div>
  <div class="rule" style="left:96px;top:14px;height:62px"></div>
  <div class="info" style="left:102px;top:14px"><strong>Ruth Benning</strong><br>Attorney<br>2847 Tamworth Lane<br>Suite 3405<br>Harlow Ridge, GA 30582<br>ruthbenningesq@quillpost.net<br>www.marlowelegaloffice.com</div>
  <div class="stripe" style="height:5px"></div>
</div>

<!-- business card front, alternate -->
<div class="sheet card" style="left:264px;top:82px;width:186px;height:98px">
  <div class="info" style="left:70px;top:8px;text-align:left"><strong>Ruth Benning</strong><br>Attorney</div>
  <div class="brand" style="position:absolute;left:10px;top:36px;font-size:14px"><span class="dot" style="width:18px;height:18px"></span><span><small>The</small><b>Marlowe</b><small>Legal Group, P.C.</small></span></div>
  <div class="info" style="left:10px;top:74px">ruthbenningesq@quillpost.net · www.marlowelegaloffice.com</div>
  <div class="stripe" style="height:5px"></div>
</div>

<!-- business card back, blue -->
<div class="sheet card blue" style="left:67px;top:185px;width:190px;height:98px">
  <div class="brand" style="position:absolute;left:26px;top:30px;font-size:14px"><span class="dot" style="width:20px;height:20px"></span><span><small>The</small><b>Marlowe</b><small>Legal Group, P.C.</small></span></div>
</div>

<!-- business card back, white -->
<div class="sheet card" style="left:264px;top:185px;width:186px;height:98px">
  <div class="brand" style="position:absolute;left:62px;top:30px;font-size:10px"><span class="dot" style="width:34px;height:34px"></span></div>
  <div class="stripe" style="height:5px"></div>
</div>

<!-- business card, blue large -->
<div class="sheet card blue" style="left:156px;top:310px;width:192px;height:110px">
  <div class="brand" style="position:absolute;left:28px;top:36px;font-size:16px"><span class="dot" style="width:22px;height:22px"></span><span><small>The</small><b>Marlowe</b><small>Legal Group, P.C.</small></span></div>
</div>

<!-- letterhead -->
<div class="sheet letterhead" style="left:566px;top:79px;width:260px;height:377px">
  <div class="brand" style="position:absolute;left:18px;top:22px;font-size:12px"><span class="dot" style="width:16px;height:16px"></span><span><small>The</small><b>Marlowe</b><small>Legal Group, P.C.</small></span></div>
  <div class="rule" style="left:104px;top:22px;height:30px"></div>
  <div class="info" style="left:110px;top:24px">2847 Tamworth Lane, Suite 3405<br>Harlow Ridge, GA 30582<br>www.marlowelegaloffice.com</div>
  <div class="stripe"></div>
</div>

<!-- fax sheet -->
<div class="sheet fax" style="left:840px;top:79px;width:262px;height:377px">
  <div class="brand" style="position:absolute;left:18px;top:22px;font-size:12px"><span class="dot" style="width:16px;height:16px"></span><span><small>The</small><b>Marlowe</b><small>Legal Group, P.C.</small></span></div>
  <div class="rule" style="left:104px;top:22px;height:30px"></div>
  <div class="info" style="left:110px;top:24px">2847 Tamworth Lane, Suite 3405<br>Harlow Ridge, GA 30582<br>www.marlowelegaloffice.com</div>
  <div class="fax-title">FAX</div>
  <div class="fax-grid">
    <span>To</span><span>&nbsp;</span><span>From</span><span>&nbsp;</span>
    <span>Fax</span><span>&nbsp;</span><span>Date</span><span>&nbsp;</span>
    <span>Pages</span><span>&nbsp;</span><span>Re</span><span>&nbsp;</span>
  </div>
  <div class="checks"><span>Urgent</span><span>For Review</span><span>Please Comment</span><span>Please Reply</span><span>Recycle</span></div>
  <div class="stripe"></div>
</div>

<!-- envelope back -->
<div class="sheet envelope-back" style="left:125px;top:533px;width:314px;height:53px;box-shadow:none;background:transparent;overflow:visible">
  <svg class="flap" width="314" height="53" viewBox="0 0 314 53" aria-hidden="true">
    <path d="M0 0 H314 V8 L170 50 Q157 54 144 50 L0 8 Z" fill="#fff" stroke="#e2e2e2"/>
    <circle cx="157" cy="30" r="10" fill="var(--navy)"/>
  </svg>
</div>

<!-- envelope front left -->
<div class="sheet envelope" style="left:5px;top:583px;width:338px;height:94px">
  <div class="brand" style="position:absolute;left:12px;top:10px;font-size:11px"><span class="dot" style="width:15px;height:15px"></span><span><small>The</small><b>Marlowe</b><small>Legal Group, P.C.</small></span></div>
  <div class="info" style="left:12px;top:48px">2847 Tamworth Lane, Suite 3405, Harlow Ridge, GA 30582</div>
  <div class="stripe" style="height:6px"></div>
</div>

<!-- envelope front right -->
<div class="sheet envelope" style="left:348px;top:583px;width:331px;height:94px">
  <div class="brand" style="position:absolute;left:12px;top:10px;font-size:11px"><span class="dot" style="width:15px;height:15px"></span><span><small>The</small><b>Marlowe</b><small>Legal Group, P.C.</small></span></div>
  <div class="rule" style="left:98px;top:12px;height:26px"></div>
  <div class="info" style="left:104px;top:14px">2847 Tamworth Lane, Suite 3405<br>Harlow Ridge, GA 30582</div>
  <div class="stripe" style="height:6px"></div>
</div>

<!-- email signature -->
<div class="sheet signature" style="left:751px;top:569px;width:286px;height:67px">
  <div class="brand" style="position:absolute;left:10px;top:14px;font-size:11px"><span class="dot" style="width:15px;height:15px"></span><span><small>The</small><b>Marlowe</b><small>Legal Group, P.C.</small></span></div>
  <div class="rule" style="left:92px;top:12px;height:36px"></div>
  <div class="info" style="left:98px;top:12px"><strong>Ruth Benning</strong><br>Attorney<br>ruthbenningesq@quillpost.net<br>www.marlowelegaloffice.com</div>
  <div class="stripe" style="height:5px"></div>
</div>

</body>
</html>
```